Corvalen Technologies Support Business Card

I would like a business card that doesn't focus on an individual role within our company but rather and call to action for current and potential clients to engage with us. We are a small business hybrid IT support company out of Metro Detroit in Michigan. Something that contains a QR code as an easy way to seek support. It should include and simple call to action but also refers to our company values. "Experience is Everything" "Obsessed with Impossible" and "Consistency Over Time Equals Trust". Our brand colors are typically a deeper/darker read, black, charcoal and white. Please see our company logo attached, and our website is is www.corvalenpc.com

```html
<!DOCTYPE html>
<html lang="en">
<head>
<meta charset="utf-8">
<title>Corvalen Technologies Support Card</title>
<link href="https://fonts.googleapis.com/css2?family=Zilla+Slab:wght@400&family=Montserrat:wght@400;600;700&display=swap" rel="stylesheet">
<style>
  :root {
    --stage: #3b3b3d;
    --card-white: #ffffff;
    --brand-red: #8f1c1d;
    --charcoal: #404040;
    --ink: #1b1b1b;
  }
  html, body {
    margin: 0;
    padding: 0;
    width: 1200px;
    height: 1059px;
    overflow: hidden;
    background: var(--stage);
  }
  .canvas {
    position: relative;
    width: 1200px;
    height: 1059px;
  }
  .card {
    position: absolute;
    border-radius: 24px;
    overflow: hidden;
  }
  .card-front {
    left: 256px; top: 100px;
    width: 688px; height: 391px;
    background: var(--card-white);
  }
  .card-back {
    left: 253px; top: 537px;
    width: 694px; height: 394px;
    background: var(--brand-red);
  }
  .wordmark {
    position: absolute;
    margin: 0;
    font-family: "Zilla Slab", serif;
    font-weight: 400;
    line-height: 1;
    letter-spacing: -0.5px;
  }
  .wordmark span { display: block; }
  .card-front .wordmark {
    left: 29px; top: 30px;
    font-size: 50px;
    color: var(--ink);
  }
  .accent-bar {
    position: absolute;
    left: 0; top: 150px;
    width: 16px; height: 46px;
    background: var(--brand-red);
  }
  .cta-title {
    position: absolute;
    left: 29px; top: 148px;
    margin: 0;
    font-family: "Montserrat", sans-serif;
    font-weight: 700;
    font-size: 24px;
    letter-spacing: 0.5px;
    line-height: 1;
    color: var(--brand-red);
  }
  .cta-text {
    position: absolute;
    left: 29px; top: 178px;
    margin: 0;
    font-family: "Montserrat", sans-serif;
    font-size: 15px;
    letter-spacing: 0.4px;
    line-height: 1;
    color: var(--ink);
  }
  .values {
    position: absolute;
    left: 29px; top: 212px;
    margin: 0; padding: 0;
    list-style: none;
    font-family: "Montserrat", sans-serif;
    font-weight: 600;
    font-size: 14px;
    letter-spacing: 0.3px;
    color: var(--charcoal);
  }
  .values li {
    display: flex;
    align-items: center;
    height: 22px;
  }
  .values li::before {
    content: "";
    width: 7px; height: 7px;
    margin-right: 10px;
    background: var(--brand-red);
    flex: none;
  }
  .contact-list {
    position: absolute;
    left: 29px; top: 293px;
    margin: 0; padding: 0;
    list-style: none;
    font-family: "Montserrat", sans-serif;
    font-size: 15px;
    letter-spacing: 0.4px;
    color: var(--ink);
  }
  .contact-list li {
    display: flex;
    align-items: center;
    height: 25px;
  }
  .contact-list svg {
    width: 13px; height: 13px;
    margin-right: 9px;
    fill: var(--brand-red);
    flex: none;
  }
  .qr-code {
    position: absolute;
    left: 438px; top: 48px;
    width: 210px; height: 210px;
    background: var(--charcoal);
    border-radius: 6px;
  }
  .qr-caption {
    position: absolute;
    left: 438px; top: 276px;
    width: 210px;
    margin: 0;
    text-align: center;
    font-family: "Montserrat", sans-serif;
    font-weight: 700;
    font-size: 15px;
    letter-spacing: 1.2px;
    line-height: 1;
    color: var(--brand-red);
  }
  .qr-note {
    position: absolute;
    left: 438px; top: 300px;
    width: 210px;
    margin: 0;
    text-align: center;
    font-family: "Montserrat", sans-serif;
    font-size: 13px;
    letter-spacing: 0.3px;
    line-height: 1.4;
    color: var(--charcoal);
  }
  .brand-square {
    position: absolute;
    left: 120px; top: 148px;
    width: 96px; height: 96px;
    background: var(--card-white);
  }
  .card-back .wordmark {
    left: 240px; top: 118px;
    font-size: 68px;
    color: var(--card-white);
  }
  .card-back .wordmark span + span { margin-top: 6px; }
</style>
</head>
<body>
<main class="canvas">
  <section class="card card-front" aria-label="Support card front">
    <h1 class="wordmark"><span>Corvalen</span><span>Technologies</span></h1>
    <div class="accent-bar" aria-hidden="true"></div>
    <p class="cta-title">NEED IT SUPPORT?</p>
    <p class="cta-text">Scan the code and we'll take it from there.</p>
    <ul class="values">
      <li>Experience is Everything</li>
      <li>Obsessed with Impossible</li>
      <li>Consistency Over Time Equals Trust</li>
    </ul>
    <ul class="contact-list">
      <li>
        <svg viewBox="0 0 16 16" aria-hidden="true"><path d="M3.6 1.2l2.2 2.9-1.3 1.6c.9 2 2.4 3.6 4.5 4.6l1.6-1.3 2.9 2.2-1.4 2.5C7.2 13.4 2.7 8.9 1.1 2.6z"/></svg>
        123-456-7890
      </li>
      <li>
        <svg viewBox="0 0 16 16" aria-hidden="true"><path d="M1 3h14v1.2L8 8.6 1 4.2z M1 5.8l7 4.4 7-4.4V13H1z"/></svg>
        support@corvalenpc.com
      </li>
      <li>
        <svg viewBox="0 0 16 16" aria-hidden="true"><path d="M8 1a7 7 0 100 14A7 7 0 008 1zm0 1.5c.8 0 1.7 1.6 2 4H6c.3-2.4 1.2-4 2-4zM2.6 6.5h2c-.1.5-.1 1-.1 1.5s0 1 .1 1.5h-2a5.6 5.6 0 010-3zm3.4 0h4c.1.5.1 1 .1 1.5s0 1-.1 1.5H6c-.1-.5-.1-1-.1-1.5s0-1 .1-1.5zm5.4 0h2a5.6 5.6 0 010 3h-2c.1-.5.1-1 .1-1.5s0-1-.1-1.5zM6 11h4c-.3 2.4-1.2 4-2 4s-1.7-1.6-2-4z"/></svg>
        www.corvalenpc.com
      </li>
    </ul>
    <div class="qr-code" role="img" aria-label="QR code linking to the Corvalen Technologies support page"></div>
    <p class="qr-caption">SCAN FOR SUPPORT</p>
    <p class="qr-note">Hybrid IT support<br>Metro Detroit, Michigan</p>
  </section>

  <section class="card card-back" aria-label="Support card back">
    <div class="brand-square" aria-hidden="true"></div>
    <h2 class="wordmark"><span>Corvalen</span><span>Technologies</span></h2>
  </section>
</main>
</body>
</html>
```